Core Value Graphic for a Service Disabled and Minority Certified contractor

My company, Keystone Aid Partners, is a US Federal Contractor that hires veterans and service disabled veterans. Our website is www.keystoneaid7.example. We work hard to maintain a 50:50 split between veterans and non-veterans on our team. Our tagline is "To Find a Better Way." We are continually looking to integrate technology and efficiency into all that we do.

I want a way to express our company core values visually so that our employees and customers alike can read them and get a sense of who we are, what drives us to succeed, and what makes up our team DNA.

I need an artist like you to help me represent our core values visually. In a manner that I can print it out on an 8"X11" sheet of paper or a large 48" X 48" poster, without losing the visual clarity or that it pixelates out of focus. I am looking for a color scheme that is patriotic with Red, White, and Blues and similar hues. I would also like to incorporate my logo and tagline into the design in some manner.

I have attached several examples of a Core Value Grids from other companies. I am hopeful it will inspire you, and a get your brain juices flowing to provide me with a knockout Core Value Grid that will rock only you can provide! I also include a copy of my company Core Values and a copy of our Logo.

Looking forward to seeing your creations. Thanks.

Target Market(s)

Employees, any potential strategic alliance partners, and customers.

Industry/Entity Type

Contractor

Requirements
Must have
• Patriotic feel and have my logo someplace on the document.

```html
<!DOCTYPE html>
<html lang="en">
<head>
<meta charset="utf-8">
<title>Keystone Aid Partners – Our Core Values</title>
<link href="https://fonts.googleapis.com/css2?family=Oswald:wght@300;400&family=Roboto:wght@400;700&family=Montserrat:wght@500;600&display=swap" rel="stylesheet">
<style>
  :root{
    --backdrop:#cccccc;
    --navy:#15304f;
    --red:#ae1118;
    --white:#ffffff;
    --ink:#1f2a44;
    --green:#d4df2a;
    --green-edge:#8fb21f;
    --blue:#29a7e1;
    --blue-edge:#1a84c4;
    --salmon:#f4887f;
    --salmon-edge:#d8423c;
    --orange:#fbb324;
    --orange-edge:#e2860e;
    --lavender:#b9aed9;
    --lavender-edge:#7a64b3;
  }
  *{box-sizing:border-box;margin:0;padding:0}
  html,body{width:1200px;height:771px;overflow:hidden;background:var(--backdrop)}
  .poster{position:absolute;left:189px;top:94px;width:822px;height:582px;background:var(--navy)}
  .tagline-band{position:absolute;left:0;top:35px;width:822px;height:36px;background:var(--red)}
  .tagline{position:absolute;left:36px;top:0;line-height:36px;font:600 21px "Montserrat",sans-serif;color:var(--white);letter-spacing:-.3px;white-space:nowrap}
  .web{position:absolute;right:232px;top:0;line-height:36px;font:400 10px "Roboto",sans-serif;color:var(--white);letter-spacing:.4px;white-space:nowrap}
  .brand-box{position:absolute;left:610px;top:19px;width:162px;height:68px;background:var(--white);display:flex;align-items:center;justify-content:center;gap:7px;padding:0 8px}
  .brand-mark{width:12px;height:12px;background:var(--red);flex:none}
  .brand-name{font:600 13px/1.15 "Montserrat",sans-serif;color:var(--navy);text-transform:uppercase}
  .values-card{position:absolute;left:34px;top:113px;width:754px;height:438px;background:var(--white);border-radius:12px}
  .values-pill{position:absolute;left:321px;top:95px;width:180px;height:32px;border-radius:16px;background:var(--red);border:2px solid var(--navy);color:var(--white);font:600 12.5px/28px "Montserrat",sans-serif;text-align:center}
  .value{position:absolute;top:144px;width:132px;height:386px;border:1.5px solid;border-radius:4px;box-shadow:0 0 0 3px rgba(255,255,255,1),0 0 0 4.5px rgba(0,0,0,.06);text-align:center;color:var(--ink)}
  .value h2{height:58px;display:flex;align-items:center;justify-content:center;padding:4px 6px 0;font:300 11.5px/1.3 "Oswald",sans-serif;color:var(--ink)}
  .value .icon{display:block;margin:2px auto 0;width:66px;height:66px}
  .copy{position:absolute;left:12px;right:12px;top:138px;font:400 6.6px/1.5 "Roboto",sans-serif}
  .copy h3{font:700 6.4px/1.6 "Roboto",sans-serif;letter-spacing:.3px;margin-top:2px}
  .value.safety{left:55px;background:var(--green);border-color:var(--green-edge)}
  .value.explore{left:200px;background:var(--blue);border-color:var(--blue-edge);color:var(--white)}
  .value.explore h2,.value.explore h3{color:var(--white)}
  .value.wingman{left:345px;background:var(--salmon);border-color:var(--salmon-edge)}
  .value.learn{left:489px;background:var(--orange);border-color:var(--orange-edge)}
  .value.troops{left:634px;background:var(--lavender);border-color:var(--lavender-edge)}
</style>
</head>
<body>
<main class="poster">
  <header class="tagline-band">
    <h1 class="tagline">TO FIND A BETTER WAY</h1>
    <span class="web">www.keystoneaid7.example</span>
  </header>
  <div class="brand-box"><span class="brand-mark"></span><span class="brand-name">Keystone Aid<br>Partners</span></div>

  <section class="values-card"></section>
  <div class="values-pill">OUR CORE VALUES</div>

  <article class="value safety">
    <h2>Everyone comes<br>back to the Green Zone</h2>
    <svg class="icon" viewBox="0 0 66 66" role="img" aria-label="Tree inside circular green arrows"><circle cx="33" cy="33" r="28" fill="#3aa63c"/></svg>
    <div class="copy">
      <h3>WHAT IT MEANS</h3>
      <p>Safety takes precedence over every phase of the day's operation.</p>
      <h3>HOW TO EXPRESS IT</h3>
      <p>Anyone can call a stop to the work in progress if an unsafe act is occurring. In fact, it is each team member's duty to do so, rectify the unsafe issue, then proceed. Never hesitate; everyone comes back. Finally, each After Action Review begins with discussing safety issues. We always let everyone on the team know of an unsafe situation, so it can be avoided in the future.</p>
      <h3>RESULT</h3>
      <p>All team members go home to their loved ones each day to pursue their individual</p>
    </div>
  </article>

  <article class="value explore">
    <h2>Boldly go. Seek. Find.</h2>
    <svg class="icon" viewBox="0 0 66 66" role="img" aria-label="Binoculars on a light blue circle"><circle cx="33" cy="33" r="28" fill="#7cc6ef"/></svg>
    <div class="copy">
      <h3>WHAT IT MEANS</h3>
      <p>We weave innovation into the fabric that makes up our company.</p>
      <h3>HOW TO EXPRESS IT</h3>
      <p>We're early adopters of technology. We quickly evaluate new technologies or processes that could separate us from our competition. Then we implement and evaluate these new technologies. We dump it quickly if we see it is not helping us achieve "Commander's Intent." We have the guts to be first. We iterate continuously and attack, attack, attack.</p>
      <h3>RESULT</h3>
      <p>We will be ahead of our competition. It' one mechanism that helps us scale. Prosperity</p>
    </div>
  </article>

  <article class="value wingman">
    <h2>Never leave your<br>wingman</h2>
    <svg class="icon" viewBox="0 0 66 66" role="img" aria-label="Team member figure on a red circle"><circle cx="33" cy="33" r="28" fill="#e8463f"/></svg>
    <div class="copy">
      <h3>WHAT IT MEANS</h3>
      <p>We always help your team members be successful. Commitment to each other and to our own personal integrity is the fuel that empowers us.</p>
      <h3>HOW TO EXPRESS IT</h3>
      <p>If a Wingman is having challenges accomplishing their individual priorities or completing their assigned mission, volunteer to help them to do so. This goes for Subs/Suppliersas well.We help those who help us succeed! Always look to establish the best win-win relationship possible, and do what you can to support them if they get into a bind.</p>
      <h3>RESULT</h3>
      <p>Be there for them and they will be there for us.</p>
    </div>
  </article>

  <article class="value learn">
    <h2>Fail<br>quickly and learn</h2>
    <svg class="icon" viewBox="0 0 66 66" role="img" aria-label="Open book on a yellow circle"><circle cx="33" cy="33" r="28" fill="#f6e11c"/></svg>
    <div class="copy">
      <h3>WHAT IT MEANS</h3>
      <p>If you're not making mistakes, you're not taking enough chances or getting out of your comfort zone.</p>
      <h3>HOW TO EXPRESS IT</h3>
      <p>Use your best judgment when trying something new. But, don't let your pride keep you from saying, "I was wrong" when your idea doesn't work. We trust you will know when it's time to dump the idea, or stop doing something that doesn't work.</p>
      <h3>RESULT</h3>
      <p>No one will ever be penalized for making a mistake. Don't be afraid to try something you believe will work. That's how we grow ourselves and our team members.</p>
    </div>
  </article>

  <article class="value troops">
    <h2>Troops (Team Members)<br>eat first</h2>
    <svg class="icon" viewBox="0 0 66 66" role="img" aria-label="Leader with team members inside a circle"><circle cx="33" cy="33" r="28" fill="#6f55ad"/></svg>
    <div class="copy">
      <h3>WHAT IT MEANS</h3>
      <p>No leader will put themselves ahead of their subordinates.</p>
      <h3>HOW TO EXPRESS IT</h3>
      <p>We lead by example. Demonstrate the moral courage and discipline to do the right thing at the highest level of quality.</p>
      <h3>RESULT</h3>
      <p>Every new team member's will quickly realize their leaders genuinely care for their welfare and success This is the best way to drive Esprit de Corps and achieve excellence.</p>
    </div>
  </article>
</main>
</body>
</html>
```